Making a tote bag entitled "shopping is hard" *

want to get a simple shopping bag designed with the lettering of "shopping is hard, i want to go do math". need to choose font(s), color(s), as well as any other art that may go around it.

Target Market(s)

studious girls and women, and their supporters

Colors

Designer to choose colors to be used in the design.

```html
<!DOCTYPE html>
<html lang="en">
<head>
<meta charset="utf-8">
<title>Shopping Is Hard – Tote Design</title>
<link rel="stylesheet" href="https://fonts.googleapis.com/css2?family=Saira+Extra+Condensed:wght@800&display=swap">
<style>
  :root {
    --paper: #ffffff;
    --ink-black: #0b0b0b;
    --ink-navy: #0a3068;
    --ink-red: #c41416;
  }
  html, body {
    margin: 0;
    padding: 0;
    width: 1200px;
    height: 1075px;
    overflow: hidden;
    background: var(--paper);
  }
  .tote-design {
    display: block;
    width: 1200px;
    height: 1075px;
  }
  .slogan {
    font-family: "Saira Extra Condensed", "Arial Narrow", sans-serif;
    font-weight: 800;
    text-transform: uppercase;
  }
  .slogan--vertical { fill: var(--ink-black); }
  .slogan--navy { fill: var(--ink-navy); }
  .slogan--red { fill: var(--ink-red); }
</style>
</head>
<body>
<svg class="tote-design" viewBox="0 0 1200 1075" xmlns="http://www.w3.org/2000/svg" aria-label="Shopping is hard, I want to go do math">
  <rect width="1200" height="1075" fill="var(--paper)"/>

  <g transform="translate(165 90) rotate(90)">
    <text class="slogan slogan--vertical" x="0" y="0" font-size="314"
          textLength="870" lengthAdjust="spacingAndGlyphs">Shopping</text>
  </g>

  <text class="slogan slogan--navy" x="400" y="260" font-size="285"
        textLength="575" lengthAdjust="spacingAndGlyphs">I want</text>
  <text class="slogan slogan--navy" x="410" y="545" font-size="390"
        textLength="560" lengthAdjust="spacingAndGlyphs">To go</text>
  <text class="slogan slogan--navy" x="400" y="740" font-size="257"
        textLength="575" lengthAdjust="spacingAndGlyphs">Do math</text>
  <text class="slogan slogan--red" x="400" y="1010" font-size="370"
        textLength="575" lengthAdjust="spacingAndGlyphs">Is hard</text>
</svg>
</body>
</html>
```